wombat paving

hay i have like a template of the site id like an can we just make it so i can edit all pictures an txt a will

also can my domain be
wombatpaving.com.au

is this even the right place for this ?

Target Market(s)

everyone

Industry/Entity Type

Domain

Requirements
Must have
• everytings ready to go i think

```html
<!DOCTYPE html>
<html lang="en">
<head>
<meta charset="utf-8">
<title>Wombat Paving</title>
<link rel="stylesheet" href="https://fonts.googleapis.com/css2?family=Jost:wght@200;300;400;500&display=swap">
<style>
:root{
  --tan:#9a8470;
  --tan-panel:rgba(122,104,88,.88);
  --ink:#1f1f1f;
  --white:#ffffff;
  --dark:#141414;
  --card:#ebebeb;
  --button:#3a3a3a;
  --muted:#555555;
  --font:"Jost", "Helvetica Neue", Arial, sans-serif;
}
*{box-sizing:border-box;margin:0;padding:0}
html,body{width:1200px;height:2353px;overflow:hidden}
body{font-family:var(--font);color:var(--ink);background:var(--white);position:relative}
a{color:inherit;text-decoration:none}

/* header */
.site-header{position:absolute;left:0;top:0;width:1200px;height:113px;background:var(--white)}
.brand{position:absolute;left:111px;top:38px;display:flex;align-items:center;gap:10px;font-size:20px;font-weight:500;letter-spacing:.5px;color:var(--tan)}
.brand-dot{width:30px;height:30px;border-radius:50%;background:var(--tan)}
.main-nav{position:absolute;top:46px;left:0;font-size:19px;font-weight:500;letter-spacing:.5px}
.main-nav a{position:absolute;white-space:nowrap}
.main-nav .is-active{color:var(--tan)}

/* hero */
.hero{position:absolute;left:0;top:113px;width:1200px;height:555px}
.hero-photo{position:absolute;inset:0;background:
  radial-gradient(ellipse 260px 320px at 300px 200px, rgba(210,95,30,.55), transparent 70%),
  linear-gradient(180deg,#2c2a28 0%,#4a4744 55%,#8c8986 100%)}
.hero-panel{position:absolute;left:624px;top:185px;width:463px;height:226px;background:var(--tan-panel);padding:38px 0 0 28px;color:var(--white)}
.hero-title{font-size:50px;font-weight:300;line-height:1;color:#151515;letter-spacing:.5px}
.hero-text{font-size:23px;font-weight:400;line-height:26px;margin-top:10px}
.hero-dots{display:flex;gap:13px;margin-top:17px}
.hero-dots span{width:14px;height:14px;border-radius:50%;border:2px solid #151515}
.hero-dots .is-current{border-color:#e2761f}

/* quote band */
.quote-band{position:absolute;left:0;top:668px;width:1200px;height:110px;display:flex;align-items:center;justify-content:center;font-size:40px;font-weight:300;letter-spacing:.3px}
.quote-phone{color:var(--tan);margin-left:12px}

/* services */
.services{position:absolute;left:0;top:778px;width:1200px;height:604px;background:var(--dark)}
.section-kicker{position:absolute;left:0;top:62px;width:1200px;text-align:center;font-size:23px;font-weight:300;color:var(--tan)}
.service{position:absolute;top:129px;width:309px}
.service-image{width:309px;height:212px}
.service-title{font-size:25px;font-weight:300;color:var(--tan);margin-top:24px}
.service-text{font-size:15px;line-height:26px;color:#e6e6e6;margin-top:16px;font-weight:300}

/* projects */
.projects-title{position:absolute;left:0;top:1420px;width:1200px;text-align:center;font-size:25px;font-weight:400}
.project{position:absolute;top:1487px;width:225px;height:339px;background:var(--card)}
.project-image{width:225px;height:144px}
.project-body{padding:17px 13px 0 13px}
.project-name{font-size:11px;font-weight:500;color:var(--tan);line-height:17px}
.project-place{font-size:11px;line-height:15px}
.project-text{font-size:11.5px;line-height:17px;margin-top:13px;color:#333}
.project-button{display:inline-block;margin-top:12px;background:var(--button);color:var(--white);font-size:11px;padding:5px 15px;line-height:17px}

/* testimonials */
.testimonials{position:absolute;left:0;top:1882px;width:1200px;height:356px}
.testimonials-photo{position:absolute;inset:0;background:linear-gradient(180deg,#0f0f10 0%,#1b1c1e 55%,#2a2824 100%)}
.testimonials-heading{position:absolute;left:436px;top:52px;font-size:24px;font-weight:400;color:var(--white)}
.testimonials-arrows{position:absolute;left:1052px;top:56px;display:flex;gap:12px}
.person-photo{position:absolute;left:179px;top:102px;width:216px;height:216px;border-radius:50%;background:radial-gradient(circle at 50% 70%,#e8892d 0%,#d27a30 35%,#f4f4f4 36%,#ffffff 100%)}
.quote-mark{position:absolute;left:438px;top:112px}
.person-name{position:absolute;left:442px;top:136px;font-size:40px;font-weight:200;color:var(--tan)}
.person-quote{position:absolute;left:442px;top:196px;width:620px;font-size:20px;line-height:26px;font-weight:300;color:#f0f0f0}

/* footer */
.site-footer{position:absolute;left:0;top:2238px;width:1200px;height:115px;background:var(--white)}
.footer-links{position:absolute;left:111px;top:44px;font-size:15px;display:flex;gap:14px;white-space:nowrap}
.footer-links .sep{color:#333}
.footer-social{position:absolute;left:1019px;top:46px;display:flex;gap:32px}
.footer-social span{width:22px;height:22px;border-radius:50%;background:#333}
</style>
</head>
<body>

<header class="site-header">
  <a class="brand" href="#"><span class="brand-dot"></span>WOMBAT PAVING</a>
  <nav class="main-nav">
    <a class="is-active" href="#" style="left:631px">HOME</a>
    <a href="#" style="left:737px">GALLERY</a>
    <a href="#" style="left:864px">SERVICES</a>
    <a href="#" style="left:1001px">CONTACT</a>
  </nav>
</header>

<section class="hero">
  <div class="hero-photo" role="img" aria-label="Road workers in orange hi-vis trousers and boots standing on fresh asphalt"></div>
  <div class="hero-panel">
    <h1 class="hero-title">WOMBAT PAVING</h1>
    <p class="hero-text">We are road maintenance and<br>construction company</p>
    <div class="hero-dots"><span class="is-current"></span><span></span><span></span><span></span></div>
  </div>
</section>

<section class="quote-band">CALL TODAY FOR A FREE QUOTE <span class="quote-phone">0412 345 678</span></section>

<section class="services">
  <h2 class="section-kicker">What We Do ?</h2>
  <article class="service" style="left:111px">
    <div class="service-image" role="img" aria-label="Warning sign seen through a wet car windscreen" style="background:linear-gradient(135deg,#8fb7b3,#3f6e6c 60%,#243c3b)"></div>
    <h3 class="service-title">Warning</h3>
    <p class="service-text">Lorem Ipsum is simply dummy text of the printing and typesetting industry. Lorem Ipsum has been the industry's standard dummy text ever since the 1500s .</p>
  </article>
  <article class="service" style="left:445px">
    <div class="service-image" role="img" aria-label="Workers in orange spreading fresh asphalt" style="background:linear-gradient(180deg,#c9773a 0%,#6a6a5a 45%,#2d2d30 100%)"></div>
    <h3 class="service-title">Road Construction</h3>
    <p class="service-text">Lorem Ipsum is simply dummy text of the printing and typesetting industry. Lorem Ipsum has been the industry's standard dummy text ever since the 1500s .</p>
  </article>
  <article class="service" style="left:780px">
    <div class="service-image" role="img" aria-label="Worker beside a paving machine releasing steam" style="background:linear-gradient(90deg,#f2f2f2 0%,#b8b8b8 40%,#3a3a3a 100%)"></div>
    <h3 class="service-title">Road Works</h3>
    <p class="service-text">Lorem Ipsum is simply dummy text of the printing and typesetting industry. Lorem Ipsum has been the industry's standard dummy text ever since the 1500s .</p>
  </article>
</section>

<h2 class="projects-title">Recent Projects</h2>

<article class="project" style="left:111px">
  <div class="project-image" role="img" aria-label="Road roller on a dark worksite with zoom icon" style="background:#2b2b2b;position:relative">
    <svg width="225" height="144" viewBox="0 0 225 144" aria-hidden="true"><circle cx="110" cy="70" r="10" fill="none" stroke="#e0a21c" stroke-width="4"/><line x1="117" y1="77" x2="126" y2="86" stroke="#e0a21c" stroke-width="5" stroke-linecap="round"/><line x1="105" y1="70" x2="115" y2="70" stroke="#e0a21c" stroke-width="3"/><line x1="110" y1="65" x2="110" y2="75" stroke="#e0a21c" stroke-width="3"/></svg>
  </div>
  <div class="project-body">
    <p class="project-name">Road Project 1</p><p class="project-place">London</p>
    <p class="project-text">Lorem Ipsum is simply dummy text of the printing and typesetting industry. Lorem Ipsum has been the industry's standard dummy text ever.</p>
    <a class="project-button" href="#">Read More</a>
  </div>
</article>
<article class="project" style="left:362px">
  <div class="project-image" role="img" aria-label="Workers in yellow hi-vis suits beside a red truck" style="background:linear-gradient(180deg,#b52a2a 0%,#c9d23a 55%,#5a5a5a 100%)"></div>
  <div class="project-body">
    <p class="project-name">Road Project 1</p><p class="project-place">London</p>
    <p class="project-text">Lorem Ipsum is simply dummy text of the printing and typesetting industry. Lorem Ipsum has been the industry's standard dummy text ever.</p>
    <a class="project-button" href="#">Read More</a>
  </div>
</article>
<article class="project" style="left:612px">
  <div class="project-image" role="img" aria-label="Grader working on a new road under a blue sky" style="background:linear-gradient(180deg,#7fa6c8 0%,#b7b3a4 50%,#4c5560 100%)"></div>
  <div class="project-body">
    <p class="project-name">Road Project 1</p><p class="project-place">London</p>
    <p class="project-text">Lorem Ipsum is simply dummy text of the printing and typesetting industry. Lorem Ipsum has been the industry's standard dummy text ever.</p>
    <a class="project-button" href="#">Read More</a>
  </div>
</article>
<article class="project" style="left:863px">
  <div class="project-image" role="img" aria-label="Worker installing steel guard rail posts" style="background:linear-gradient(90deg,#3e5a8a 0%,#9aa3ab 55%,#c7ccd0 100%)"></div>
  <div class="project-body">
    <p class="project-name">Road Project 1</p><p class="project-place">London</p>
    <p class="project-text">Lorem Ipsum is simply dummy text of the printing and typesetting industry. Lorem Ipsum has been the industry's standard dummy text ever.</p>
    <a class="project-button" href="#">Read More</a>
  </div>
</article>

<section class="testimonials">
  <div class="testimonials-photo" role="img" aria-label="Dark road landscape at dusk"></div>
  <h2 class="testimonials-heading">Testimonials</h2>
  <div class="testimonials-arrows">
    <svg width="12" height="14" viewBox="0 0 12 14" aria-label="Previous"><polyline points="8,2 3,7 8,12" fill="none" stroke="#fff" stroke-width="2"/></svg>
    <svg width="12" height="14" viewBox="0 0 12 14" aria-label="Next"><polyline points="4,2 9,7 4,12" fill="none" stroke="#fff" stroke-width="2"/></svg>
  </div>
  <div class="person-photo" role="img" aria-label="Portrait of a smiling worker in a hard hat and orange vest"></div>
  <svg class="quote-mark" width="30" height="22" viewBox="0 0 30 22" aria-hidden="true"><path d="M2 22V12C2 5 6 1 12 0v4c-3 1-5 3-5 7h5v11zM18 22V12c0-7 4-11 10-12v4c-3 1-5 3-5 7h5v11z" fill="#e2761f"/></svg>
  <p class="person-name">Daniel Harlow</p>
  <p class="person-quote">Lorem Ipsum is simply dummy text of the printing and typesetting industry. Lorem Ipsum has been the industry's standard dummy text ever since the 1500s, when an unknown printer took a galley of type and scrambled it to make a type specimen book.</p>
</section>

<footer class="site-footer">
  <nav class="footer-links">
    <a href="#">Home</a><span class="sep">|</span>
    <a href="#">Gallery</a><span class="sep">|</span>
    <a href="#">Services</a><span class="sep">|</span>
    <a href="#">Contact</a><span class="sep">|</span>
    <span>© copyright 2015. All rights reserved.</span>
  </nav>
  <div class="footer-social"><span aria-label="Social link"></span><span aria-label="Social link"></span></div>
</footer>

</body>
</html>
```